Mexican Restaurant needs a new Menu Design

Mexican restaurant LAS TORTUGAS is renewing its menu, so we need something new.
Since our inception we have given the task of rescuing ingredients, recipes, and traditional and representatives dishes of the culinary techniques of yesteryear.
We are the only restaurant in Guadalajara that manufactures its own dairy natural as fresh cheese, the cream and our already well-known and traditional jocoqui. In addition, we produce organic ranch egg and are currently in the development of organic vegetables cultivated on the slopes of the old Hill which gives our plants benefit from an exceptional microclimate.
Find more information about the restaurant in www.lastortugasfonda.example.
The menu needs to have the full list of products with the prices, some phrases that speak of the philosophy of the ranch-style-living, photos.
We need the cover, back cover and interiors.
Updates
Thank you so much for the proposals you have submitted for the menu design. We are looking them carefully.
Thank you very much for taking your time to design a proposal for our menu!!!
Target Market(s)
The target is very wide (28-40 yrs.): Young executives, Young families, Housewives.
Industry/Entity Type
Restaurant
Look and feel
Each slider illustrates characteristics of the customer's brand and the style your logo design should communicate.

```html
<!DOCTYPE html>
<html lang="es">
<head>
<meta charset="utf-8">
<title>Las Tortugas · Postres y Bebidas</title>
<link href="https://fonts.googleapis.com/css2?family=Marcellus&family=Cabin:wght@400&family=Alegreya:wght@700&display=swap" rel="stylesheet">
<style>
:root{
  --canvas:#eeeeee;
  --paper-light:#f6e9c8;
  --paper-mid:#efdcaf;
  --paper-dark:#e4c88f;
  --frame:#e3241b;
  --label:#d9231a;
  --ink:#2a2118;
  --ink-soft:#3b3026;
  --rule:#4a4038;
}
*{margin:0;padding:0;box-sizing:border-box}
html,body{width:1200px;height:901px;overflow:hidden;background:var(--canvas)}
.spread{position:relative;width:1200px;height:901px}
.page{position:absolute;top:30px;width:570px;height:827px;
  background:radial-gradient(ellipse at 30% 25%,var(--paper-light),var(--paper-mid) 60%,var(--paper-dark));
  overflow:hidden}
.page--left{left:22px}
.page--right{left:608px}
.page::after{content:"";position:absolute;left:0;top:0;right:0;bottom:102px;border:4px solid var(--frame);border-bottom:none;pointer-events:none}
.page-number{position:absolute;top:8px;right:16px;font:16px "Marcellus",serif;color:var(--ink-soft)}
.section-label{position:absolute;left:20px;height:36px;padding:0 12px;
  background:var(--label);border-radius:6px 14px 8px 12px;
  font:700 27px/36px "Alegreya",serif;color:#fff}
.item{position:absolute;left:16px;right:20px}
.page--right .item{left:18px;right:16px}
.item-head{display:flex;justify-content:space-between;align-items:flex-end;
  height:26px;border-bottom:1px solid var(--rule);padding:0 2px 2px}
.item-name{font:18px "Marcellus",serif;color:var(--ink)}
.item-price{font:16px "Marcellus",serif;color:var(--ink);letter-spacing:.5px}
.item-desc{margin-top:4px;padding:0 2px;font:13px/17px "Cabin",sans-serif;color:var(--ink-soft)}
.photo-strip{position:absolute;left:0;bottom:0;width:570px;height:102px;display:flex}
.photo{flex:1;height:100%}
.ph-cake{background:radial-gradient(circle,#f4f0ea 30%,#5a2a1c 75%)}
.ph-flan{background:radial-gradient(ellipse,#d99a3a 20%,#f4f0ea 45%,#4a2418 80%)}
.ph-fruit-bread{background:radial-gradient(circle,#b8642c 30%,#7a3a1c 60%,#3a1c12)}
.ph-bread-basket{background:radial-gradient(circle,#c98b4a 25%,#b52a1e 55%,#3a1c12)}
.ph-horchata{background:linear-gradient(135deg,#e08a2a,#f1ece0 45%,#c9482a)}
.ph-coffee{background:radial-gradient(circle,#8a5a2a 15%,#f4f2ee 35%,#4a2e1a 75%)}
.ph-olla{background:radial-gradient(circle,#d9c4a2 20%,#6a3a22 50%,#c7b48f)}
.ph-margarita{background:radial-gradient(circle,#f1f0d8 25%,#8fb23a 55%,#e07a1a)}
</style>
</head>
<body>
<div class="spread">

  <section class="page page--left">
    <div class="page-number">page 11</div>
    <h2 class="section-label" style="top:20px">Postres</h2>

    <div class="item" style="top:60px"><div class="item-head"><span class="item-name">Carlota</span><span class="item-price">00.00</span></div>
      <p class="item-desc">Dice el Obispo que es un "Bocatto Di Cardenale". Crujiente de Dulce de Limón con base de Galletas Marías con Dos bolas de Gelatto de Vainilla y un toque de Salsa de Chocolate.</p></div>

    <div class="item" style="top:150px"><div class="item-head"><span class="item-name">Pastel de Elote con Miel de Abeja</span><span class="item-price">00.00</span></div>
      <p class="item-desc">Esponjosito Pay Horneao de Elotitos Tiernos con un toque de Miel de Abeja de San Miguel.</p></div>

    <div class="item" style="top:222px"><div class="item-head"><span class="item-name">Flan Casero "Doña Rosario"</span><span class="item-price">00.00</span></div>
      <p class="item-desc">Muy Casero. Muy Sabroso. Muy de LAS TORTUGAS.</p></div>

    <div class="item" style="top:276px"><div class="item-head"><span class="item-name">Fruta de Horno</span><span class="item-price">00.00</span></div>
      <p class="item-desc">Surtido de Pan Dulce Artesanal traído todos los días del meritito Tlajomulco. Más de 50 años de Tradición respaldan a este postre digno de Hacendados de Haciendas.</p></div>

    <div class="item" style="top:349px"><div class="item-head"><span class="item-name">Pay de Zarzamora</span><span class="item-price">00.00</span></div>
      <p class="item-desc">Pay de Queso con Zarzamora estilo Niú York.</p></div>

    <div class="item" style="top:403px"><div class="item-head"><span class="item-name">Platanitos Tecomán</span><span class="item-price">00.00</span></div>
      <p class="item-desc">Platanitos Macho con Azúcar y Canela, como en el Meritito Colima.</p></div>

    <h2 class="section-label" style="top:462px">Bebidas</h2>

    <div class="item" style="top:502px"><div class="item-head"><span class="item-name">Agua de Horchata</span><span class="item-price">00.00</span></div>
      <p class="item-desc">La Mejor Agua de Horchata de Jalisco con Canela Natural y "Leche La Vaquita".</p></div>

    <div class="item" style="top:553px"><div class="item-head"><span class="item-name">Agua de Jamaica</span><span class="item-price">00.00</span></div>
      <p class="item-desc">Con Jamaica Puramente Natural.</p></div>

    <div class="item" style="top:605px"><div class="item-head"><span class="item-name">Atole Filipino</span><span class="item-price">00.00</span></div>
      <p class="item-desc">Del de adeveras con Vainilla Natural. Se vale sopearle con Gorditas Doña Lupe o Pan Dulce.</p></div>

    <div class="item" style="top:673px"><div class="item-head"><span class="item-name">Café Espresso Gourmet</span><span class="item-price">00.00</span></div>
      <p class="item-desc">Una Mezcla Muy Gourmet de Café Seleccionado por El Patrón en Persona.</p></div>

    <div class="photo-strip">
      <div class="photo ph-cake" role="img" aria-label="Photo of a plated slice of carlota dessert"></div>
      <div class="photo ph-flan" role="img" aria-label="Photo of homemade flan on a white plate"></div>
      <div class="photo ph-fruit-bread" role="img" aria-label="Photo of a clay plate with baked fruit and sweet bread"></div>
      <div class="photo ph-bread-basket" role="img" aria-label="Photo of a basket of sweet bread on a red cloth"></div>
    </div>
  </section>

  <section class="page page--right">
    <div class="page-number">page 12</div>

    <div class="item" style="top:39px"><div class="item-head"><span class="item-name">Café de Olla</span><span class="item-price">00.00</span></div>
      <p class="item-desc">Nuestra Receta de Café de Olla es el Mejor Secreto de La Cocina. Modestamente el Mejor Café de olla del Mundo.</p></div>

    <div class="item" style="top:116px"><div class="item-head"><span class="item-name">Capuccino Convento</span><span class="item-price">00.00</span></div>
      <p class="item-desc">Sabroso Capuccino con un toque de Granadina.</p></div>

    <div class="item" style="top:170px"><div class="item-head"><span class="item-name">Chocolate Calientito</span><span class="item-price">00.00</span></div>
      <p class="item-desc">Elaborado con Puro Chocolate "Cacao del Valle" que se fabrica en Ciudad Guzmán de la misma manera desde hace 60 años.</p></div>

    <div class="item" style="top:241px"><div class="item-head"><span class="item-name">Jugo de Nopal</span><span class="item-price">00.00</span></div>
      <p class="item-desc">Un Jugo Ampliamente recomendable por los Nutriólogos de Ora y Los Abuelos dendenantes.</p></div>

    <div class="item" style="top:314px"><div class="item-head"><span class="item-name">Jugo de Zanahoria</span><span class="item-price">00.00</span></div>
      <p class="item-desc">Elaborado al momento con Pura Zanahoria Natural.</p></div>

    <div class="item" style="top:369px"><div class="item-head"><span class="item-name">Jugo de Toronja</span><span class="item-price">00.00</span></div>
      <p class="item-desc">Elaborado al momento con Pura Toronja Natural.</p></div>

    <div class="item" style="top:424px"><div class="item-head"><span class="item-name">Jugo de Lima</span><span class="item-price">00.00</span></div>
      <p class="item-desc">Elaborado al momento con Pura Lima Natural.</p></div>

    <div class="item" style="top:478px"><div class="item-head"><span class="item-name">Jugo de Naranja</span><span class="item-price">00.00</span></div>
      <p class="item-desc">Elaborado al momento con Pura Naranja Natural.</p></div>

    <div class="item" style="top:535px"><div class="item-head"><span class="item-name">Margarita de Limón</span><span class="item-price">00.00</span></div>
      <p class="item-desc">Va "Frappé" y puede ser con el Tequila de su Elección.</p></div>

    <div class="item" style="top:591px"><div class="item-head"><span class="item-name">Margarita de Tamarindo</span><span class="item-price">00.00</span></div>
      <p class="item-desc">Va "Frappé" Con el Tequila de su Preferencia.</p></div>

    <div class="item" style="top:645px"><div class="item-head"><span class="item-name">Margarita de Fresa</span><span class="item-price">00.00</span></div>
      <p class="item-desc">¡ Efectivamente, Muy Fresa !</p></div>

    <div class="photo-strip">
      <div class="photo ph-horchata" role="img" aria-label="Photo of a glass of horchata surrounded by fruit"></div>
      <div class="photo ph-coffee" role="img" aria-label="Photo of an espresso cup on coffee beans"></div>
      <div class="photo ph-olla" role="img" aria-label="Photo of a clay mug of café de olla"></div>
      <div class="photo ph-margarita" role="img" aria-label="Photo of a margarita glass with citrus fruit"></div>
    </div>
  </section>

</div>
</body>
</html>
```